Skincare Cleanser Bottle Label

New product launch of a mint facial cleanser.
Brand is called Dorvelle.
Product will be called Lunara.
Looking for a label design that can be printed using silk screening.
High gloss white plastic bottle. 8oz. White push pump top.
Clinical skincare brand, professional image, sold in medical spas.

Target Market(s)

Women Age 20-65

Industry/Entity Type

Health And Wellness

Font styles to use
Serif
Sans Serif

Requirements
Must have
• Dorvelle brand name in the orignal font.
Should not have
• Multiple colours.

```html
<!DOCTYPE html>
<html lang="en">
<head>
<meta charset="utf-8">
<title>Dorvelle Lunara – Mint Facial Cleanser Label</title>
<link href="https://fonts.googleapis.com/css2?family=Josefin+Sans:wght@300&family=Source+Sans+3:ital,wght@0,400;1,700&display=swap" rel="stylesheet">
<style>
  :root {
    --page: #ececec;
    --label: #ffffff;
    --ink: #1a1a1a;
    --ink-soft: #555555;
    --rule: #8a8a8a;
    --leaf-light: #7cc07a;
    --leaf-dark: #2f7d3a;
  }
  html, body {
    margin: 0;
    width: 900px;
    height: 1200px;
    overflow: hidden;
    background: var(--page);
  }
  .label {
    position: absolute;
    left: 150px;
    top: 100px;
    width: 600px;
    height: 1000px;
    background: var(--label);
    border-radius: 6px;
  }
  .leaf-art {
    position: absolute;
    left: 150px;
    top: 120px;
    width: 170px;
    height: 150px;
    background: radial-gradient(circle at 45% 40%, var(--leaf-light), var(--leaf-dark));
    border-radius: 4px;
  }
  .leaf-frame {
    position: absolute;
    left: 120px;
    top: 100px;
    width: 220px;
    height: 210px;
  }
  .product-tab {
    position: absolute;
    left: 300px;
    top: 238px;
    width: 300px;
    height: 62px;
    background: var(--ink);
    display: flex;
    align-items: center;
    padding-left: 22px;
    box-sizing: border-box;
  }
  .product-name {
    font-family: "Source Sans 3", sans-serif;
    font-style: italic;
    font-weight: 700;
    font-size: 44px;
    color: var(--label);
    letter-spacing: -0.5px;
  }
  .product-type {
    position: absolute;
    left: 322px;
    top: 312px;
    font-family: "Source Sans 3", sans-serif;
    font-size: 20px;
    line-height: 1.15;
    color: var(--ink-soft);
  }
  .brand-name {
    position: absolute;
    left: 118px;
    top: 270px;
    height: 560px;
    writing-mode: vertical-rl;
    transform: rotate(180deg);
    font-family: "Josefin Sans", sans-serif;
    font-weight: 300;
    font-size: 140px;
    line-height: 1;
    color: var(--ink);
    letter-spacing: 2px;
  }
  .footer-rule {
    position: absolute;
    left: 130px;
    top: 870px;
    width: 200px;
    height: 1px;
    background: var(--rule);
  }
  .tagline, .volume {
    position: absolute;
    left: 132px;
    font-family: "Source Sans 3", sans-serif;
    font-size: 22px;
    color: var(--ink-soft);
  }
  .tagline { top: 880px; }
  .volume { top: 930px; }
</style>
</head>
<body>
  <main class="label">
    <svg class="leaf-frame" viewBox="0 0 220 210" aria-hidden="true">
      <path d="M30 20 V190 Q30 200 40 200 H120" fill="none" stroke="#8a8a8a" stroke-width="2"/>
    </svg>
    <div class="leaf-art" role="img" aria-label="Fresh mint leaves sprig"></div>
    <div class="product-tab"><span class="product-name">lunara</span></div>
    <p class="product-type" style="margin:0">mint facial<br>cleanser</p>
    <h1 class="brand-name" style="margin:0">dorvelle</h1>
    <div class="footer-rule"></div>
    <p class="tagline" style="margin:0">lorem ipsum</p>
    <p class="volume" style="margin:0">250 ml</p>
  </main>
</body>
</html>
```